Custom Mexican Train Dominos Scorecard

My wife and I regularly play Mexican Train dominos with our friends and family and would like to create a series of custom scorecards specific to our various groups that we play with. The idea would be to have them printed on pads or in notebooks that over time will hold a record of all of our games. Searching around on the web, the only "off the shelf" that I see are pretty plain and boring (see attached). We would love something with a fun and playful mid-century graphic feel to it. Can be a single color or more than one. We want to have the player names incorporated into the design, so for the first one the names would be Carla, Douglas, Ruth & Oliver. We will want a place to date each card and of course boxes to fill out the score. I have included a few examples of how the scorecard is basically laid out. Can be any size and can be done in landscape or portrait. I think I would just like the title to say "Domino Night" or potentially no title at all with just a fun domino graphic. Thank you!

Requirements
Must have
• Basic score layout
Nice to have
• nothing in particular
Should not have
• nothing in particular

```html
<!DOCTYPE html>
<html lang="en">
<head>
<meta charset="utf-8">
<title>Domino Night Scorecard</title>
<link rel="stylesheet" href="https://fonts.googleapis.com/css2?family=Antonio:wght@400&family=Lobster&display=swap">
<style>
  :root {
    --page-bg: #d3d3d3;
    --purple-deep: #662d91;
    --purple-mid: #8c62ae;
    --purple-light: #c3abd8;
    --label-blue: #a9dce8;
    --cell-blue: #d9eef5;
    --ink: #231f20;
    --white: #ffffff;
    --title-yellow: #ffe600;
  }
  * { box-sizing: border-box; margin: 0; padding: 0; }
  html, body { width: 960px; height: 1200px; overflow: hidden; background: var(--page-bg); }

  .scorecard {
    position: absolute; left: 107px; top: 140px; width: 718px; height: 952px;
    background: var(--white);
    border: 1px solid var(--ink);
    box-shadow: 4px 5px 6px rgba(0,0,0,0.35);
    overflow: hidden;
  }

  .header {
    position: absolute; left: 0; top: 0; width: 100%; height: 131px;
    background: linear-gradient(to bottom, var(--purple-deep), var(--purple-light));
  }
  .header-art { position: absolute; border-radius: 14px; background: rgba(255,255,255,0.28); }
  .header-art--dominoes { left: 28px; top: 28px; width: 110px; height: 84px; }
  .header-art--drink { left: 585px; top: 15px; width: 120px; height: 104px;
    background: linear-gradient(to bottom, rgba(255,230,0,0.45), rgba(230,150,90,0.55)); }
  .title {
    position: absolute; left: 150px; top: 33px; width: 420px; text-align: center;
    font-family: "Antonio", sans-serif; font-weight: 400; font-size: 64px; line-height: 1;
    letter-spacing: 1px; color: var(--title-yellow);
  }

  .rule { position: absolute; left: 0; width: 100%; height: 0; border-top: 1px solid var(--ink); }

  .row {
    position: absolute; left: 0; width: 100%; height: 36px;
    display: grid; grid-template-columns: 144px repeat(4, 1fr);
    background: var(--cell-blue);
  }
  .row > div { border-left: 1px solid var(--ink); display: flex; align-items: center; justify-content: center; overflow: hidden; }
  .row > div:first-child { border-left: none; }
  .row--players { top: 139px; }
  .row--total { top: 858px; }
  .label { background: var(--label-blue); }
  .name, .label {
    font-family: "Antonio", sans-serif; font-size: 26px; line-height: 1; color: var(--ink); letter-spacing: -0.5px;
  }

  .score-table { position: absolute; left: 0; top: 189px; width: 100%; height: 655px; }
  .score-row {
    display: grid; grid-template-columns: 144px repeat(4, 1fr);
    height: 46.79px; border-bottom: 1px solid var(--ink);
  }
  .score-row:last-child { border-bottom: none; }
  .score-row > div { border-left: 1px solid var(--ink); }
  .score-row > :first-child { border-left: none; }
  .round { background: var(--cell-blue); display: flex; align-items: center; padding-left: 12px; gap: 10px; }
  .round svg { width: 78px; height: 39px; flex: none; }
  .round-number { font-family: "Lobster", cursive; font-size: 28px; line-height: 1; color: var(--ink); width: 32px; text-align: center; }
  .score-row--subtotal { background: var(--cell-blue); }
  .score-row--subtotal > .label { display: flex; align-items: center; justify-content: center; font-size: 29px; }

  .footer {
    position: absolute; left: 0; top: 901px; width: 100%; height: 51px;
    background: linear-gradient(to bottom, var(--purple-mid), var(--purple-deep));
  }
</style>
</head>
<body>
<svg width="0" height="0" style="position:absolute">
  <defs>
    <g id="pip-1"><circle cx="19" cy="19" r="3.4"/></g>
    <g id="pip-2"><circle cx="6" cy="6" r="3.4"/><circle cx="32" cy="32" r="3.4"/></g>
    <g id="pip-3"><use href="#pip-2"/><circle cx="19" cy="19" r="3.4"/></g>
    <g id="pip-4"><use href="#pip-2"/><circle cx="32" cy="6" r="3.4"/><circle cx="6" cy="32" r="3.4"/></g>
    <g id="pip-5"><use href="#pip-4"/><circle cx="19" cy="19" r="3.4"/></g>
    <g id="pip-6"><use href="#pip-4"/><circle cx="19" cy="6" r="3.4"/><circle cx="19" cy="32" r="3.4"/></g>
    <g id="pip-7"><use href="#pip-6"/><circle cx="19" cy="19" r="3.4"/></g>
    <g id="pip-8"><use href="#pip-6"/><circle cx="6" cy="19" r="3.4"/><circle cx="32" cy="19" r="3.4"/></g>
    <g id="pip-9"><use href="#pip-8"/><circle cx="19" cy="19" r="3.4"/></g>
    <g id="pip-10">
      <circle cx="5" cy="6" r="3.4"/><circle cx="14.3" cy="6" r="3.4"/><circle cx="23.7" cy="6" r="3.4"/><circle cx="33" cy="6" r="3.4"/>
      <circle cx="5" cy="32" r="3.4"/><circle cx="14.3" cy="32" r="3.4"/><circle cx="23.7" cy="32" r="3.4"/><circle cx="33" cy="32" r="3.4"/>
      <circle cx="5" cy="19" r="3.4"/><circle cx="33" cy="19" r="3.4"/>
    </g>
    <g id="pip-11"><use href="#pip-10"/><circle cx="19" cy="19" r="3.4"/></g>
    <g id="pip-12"><use href="#pip-10"/><circle cx="14.3" cy="19" r="3.4"/><circle cx="23.7" cy="19" r="3.4"/></g>
    <g id="tile">
      <rect x="0.5" y="0.5" width="77" height="38" rx="3" fill="#fff" stroke="#231f20"/>
      <line x1="39" y1="3" x2="39" y2="36" stroke="#231f20" stroke-width="2"/>
    </g>
  </defs>
</svg>

<main class="scorecard">
  <header class="header">
    <div class="header-art header-art--dominoes" role="img" aria-label="Illustration of three tilted dominoes"></div>
    <h1 class="title">Domino Night</h1>
    <div class="header-art header-art--drink" role="img" aria-label="Illustration of a glass of iced tea with a lemon slice"></div>
  </header>

  <div class="rule" style="top:131px"></div>
  <div class="rule" style="top:138px"></div>

  <div class="row row--players">
    <div class="label">Players</div>
    <div class="name">Carla</div>
    <div class="name">Douglas</div>
    <div class="name">Ruth</div>
    <div class="name">Oliver</div>
  </div>

  <div class="rule" style="top:175px"></div>
  <div class="rule" style="top:181px"></div>
  <div class="rule" style="top:188px"></div>

  <div class="score-table">
    <div class="score-row"><div class="round"><svg viewBox="0 0 78 39"><use href="#tile"/><g fill="#231f20"><use href="#pip-12" transform="translate(0.5,0.5)"/><use href="#pip-12" transform="translate(39.5,0.5)"/></g></svg><span class="round-number">12</span></div><div></div><div></div><div></div><div></div></div>
    <div class="score-row"><div class="round"><svg viewBox="0 0 78 39"><use href="#tile"/><g fill="#231f20"><use href="#pip-11" transform="translate(0.5,0.5)"/><use href="#pip-11" transform="translate(39.5,0.5)"/></g></svg><span class="round-number">11</span></div><div></div><div></div><div></div><div></div></div>
    <div class="score-row"><div class="round"><svg viewBox="0 0 78 39"><use href="#tile"/><g fill="#231f20"><use href="#pip-10" transform="translate(0.5,0.5)"/><use href="#pip-10" transform="translate(39.5,0.5)"/></g></svg><span class="round-number">10</span></div><div></div><div></div><div></div><div></div></div>
    <div class="score-row"><div class="round"><svg viewBox="0 0 78 39"><use href="#tile"/><g fill="#231f20"><use href="#pip-9" transform="translate(0.5,0.5)"/><use href="#pip-9" transform="translate(39.5,0.5)"/></g></svg><span class="round-number">9</span></div><div></div><div></div><div></div><div></div></div>
    <div class="score-row"><div class="round"><svg viewBox="0 0 78 39"><use href="#tile"/><g fill="#231f20"><use href="#pip-8" transform="translate(0.5,0.5)"/><use href="#pip-8" transform="translate(39.5,0.5)"/></g></svg><span class="round-number">8</span></div><div></div><div></div><div></div><div></div></div>
    <div class="score-row"><div class="round"><svg viewBox="0 0 78 39"><use href="#tile"/><g fill="#231f20"><use href="#pip-7" transform="translate(0.5,0.5)"/><use href="#pip-7" transform="translate(39.5,0.5)"/></g></svg><span class="round-number">7</span></div><div></div><div></div><div></div><div></div></div>
    <div class="score-row score-row--subtotal"><div class="label">Sub Total</div><div></div><div></div><div></div><div></div></div>
    <div class="score-row"><div class="round"><svg viewBox="0 0 78 39"><use href="#tile"/><g fill="#231f20"><use href="#pip-6" transform="translate(0.5,0.5)"/><use href="#pip-6" transform="translate(39.5,0.5)"/></g></svg><span class="round-number">6</span></div><div></div><div></div><div></div><div></div></div>
    <div class="score-row"><div class="round"><svg viewBox="0 0 78 39"><use href="#tile"/><g fill="#231f20"><use href="#pip-5" transform="translate(0.5,0.5)"/><use href="#pip-5" transform="translate(39.5,0.5)"/></g></svg><span class="round-number">5</span></div><div></div><div></div><div></div><div></div></div>
    <div class="score-row"><div class="round"><svg viewBox="0 0 78 39"><use href="#tile"/><g fill="#231f20"><use href="#pip-4" transform="translate(0.5,0.5)"/><use href="#pip-4" transform="translate(39.5,0.5)"/></g></svg><span class="round-number">4</span></div><div></div><div></div><div></div><div></div></div>
    <div class="score-row"><div class="round"><svg viewBox="0 0 78 39"><use href="#tile"/><g fill="#231f20"><use href="#pip-3" transform="translate(0.5,0.5)"/><use href="#pip-3" transform="translate(39.5,0.5)"/></g></svg><span class="round-number">3</span></div><div></div><div></div><div></div><div></div></div>
    <div class="score-row"><div class="round"><svg viewBox="0 0 78 39"><use href="#tile"/><g fill="#231f20"><use href="#pip-2" transform="translate(0.5,0.5)"/><use href="#pip-2" transform="translate(39.5,0.5)"/></g></svg><span class="round-number">2</span></div><div></div><div></div><div></div><div></div></div>
    <div class="score-row"><div class="round"><svg viewBox="0 0 78 39"><use href="#tile"/><g fill="#231f20"><use href="#pip-1" transform="translate(0.5,0.5)"/><use href="#pip-1" transform="translate(39.5,0.5)"/></g></svg><span class="round-number">1</span></div><div></div><div></div><div></div><div></div></div>
    <div class="score-row"><div class="round"><svg viewBox="0 0 78 39"><use href="#tile"/></svg><span class="round-number">0</span></div><div></div><div></div><div></div><div></div></div>
  </div>

  <div class="rule" style="top:844px"></div>
  <div class="rule" style="top:851px"></div>
  <div class="rule" style="top:857px"></div>

  <div class="row row--total">
    <div class="label">Game Total</div>
    <div></div><div></div><div></div><div></div>
  </div>

  <div class="rule" style="top:894px"></div>
  <div class="rule" style="top:900px"></div>

  <div class="footer"></div>
</main>
</body>
</html>
```